Help Liu Wenhao redesign his business card!

Liu Wenhao, an "influential" Chinese businessman, made international headlines this week with his business card...but not for the right reasons. Help Liu Wenhao redesign his new business card - funny and/or satirical submissions welcome!

Check out his hilarious business card that he was giving out on a trip to New York, with not one, not two...but TEN titles! Let's just say they're not the most humble titles either :).

Read more about Liu's business card here: http://blogs.brightledger.example/asiadesk/2014/01/14/liu-wenhaos-business-card-needs-to-be-recycled/

While the rest of the world is laughing at him, we want to help. This is an unofficial contest, but we'd like the PixelForge community to have a shot at redesigning Liu's business card. Thousands of businesses have used PixelForge.example to create beautiful business cards, so we know the community of designers here can do a great job.

We'd like you to create a business card worthy of this honorable businessman, while also keeping a clean, dignified design.

Funny / satirical job titles and designs are encouraged. Note you do not have to use all of Liu's titles on the card. Feel free to come up with your own creative titles!

In regard to contact details, please use dummy contact details. Liu's company name and street address are:

China Tai-Mo Reusable Scrap & Restoration Corporation
Fuxing Road 7, Lanqiao District, Nanjing, China

You can design a single sided or double-sided card - it's completely up to you!

Target Market(s)

Business people and government officials of the world

Industry/Entity Type

Business

Font styles to use
Serif
Sans Serif
Decorative

Colors
ec2027
ffc214
6b449b
0455a3

Requirements
Must have
• At least 1 title, preferably more than 1.

Designers can approach this task how they like however one option could be to use one of Liu's titles and create a suitable business card graphic to suit the role. Designers are also encouraged to o make up a new title and design a graphic to suit.

Here are the titles - but you can also make up your own!

Most influential person of China
Most prominent Philanthropist of China
China Moral Leader
China Earthquake Rescue Hero
Most well-known and Beloved Chinese Role Model
China Top Ten Most Honorable Volunteer
Most Charismatic Philanthropist of China
China Low Carbon Emission
Environmental Protection Top Advocate
China's Foremost Environmental Preservation Demolition Expert
Should not have
• No black borders around photographs of Liu Wenhao
Do not present Liu Wenhao's image in grayscale (black and white)

For a detailed guideline for colors to avoid in design targeting the Chinese market, see http://www.corvalegroup.example/2011/01/17/color/

```html
<!DOCTYPE html>
<html lang="en">
<head>
<meta charset="utf-8">
<title>Liu Wenhao — China Tai-Mo Reusable Scrap &amp; Restoration Corporation</title>
<link rel="stylesheet" href="https://fonts.googleapis.com/css2?family=Mulish:wght@400;500&display=swap">
<style>
  :root {
    --card-dark: #353537;
    --card-mid: #4a4a4c;
    --card-light: #8e8e90;
    --brand-red: #ec2027;
    --brand-yellow: #ffc214;
    --text-white: #ffffff;
    --icon-cut: #3f3f41;
  }
  html, body {
    margin: 0;
    padding: 0;
    overflow: hidden;
    background: #ffffff;
  }
  .card {
    position: relative;
    width: 668px;
    height: 1200px;
    overflow: hidden;
    background:
      radial-gradient(ellipse 110% 55% at 0% 100%, var(--card-light) 0%, var(--card-mid) 55%, rgba(53,53,55,0) 100%),
      linear-gradient(180deg, var(--card-dark) 0%, var(--card-dark) 45%, var(--card-mid) 100%);
    font-family: "Mulish", "Avenir", sans-serif;
  }
  .accent-band {
    position: absolute;
    left: 0;
    top: 0;
    width: 668px;
    height: 1200px;
  }
  .company-name {
    position: absolute;
    right: 62px;
    top: 44px;
    margin: 0;
    text-align: right;
    color: var(--brand-yellow);
    font-weight: 400;
    font-size: 42px;
    line-height: 71px;
    letter-spacing: 0.2px;
  }
  .holder {
    position: absolute;
    right: 62px;
    top: 372px;
    width: 360px;
    margin: 0;
    text-align: right;
    color: var(--text-white);
  }
  .holder-name {
    display: block;
    font-size: 30px;
    font-weight: 500;
    line-height: 40px;
  }
  .holder-title {
    display: block;
    margin-top: 8px;
    font-size: 21px;
    font-weight: 400;
    line-height: 30px;
  }
  .band-url {
    position: absolute;
    left: 138px;
    top: 736px;
    transform: translate(-50%, -50%) rotate(-90deg);
    color: var(--text-white);
    font-size: 26px;
    letter-spacing: 0.5px;
    white-space: nowrap;
  }
  .contact-list {
    position: absolute;
    left: 262px;
    top: 997px;
    margin: 0;
    padding: 0;
    list-style: none;
  }
  .contact-item {
    display: flex;
    align-items: center;
    height: 46px;
    color: var(--text-white);
    font-size: 31px;
    letter-spacing: 0.3px;
  }
  .contact-icon {
    width: 28px;
    height: 28px;
    margin-right: 20px;
    flex: none;
  }
</style>
</head>
<body>
<div class="card">
  <svg class="accent-band" viewBox="0 0 668 1200" aria-hidden="true">
    <path d="M49 122 C 120 190, 223 260, 223 370 L 223 1200 L 49 1200 Z" fill="var(--brand-red)"/>
  </svg>

  <h1 class="company-name">China Tai-Mo<br>Reusable Scrap<br>&amp; Restoration<br>Corporation</h1>

  <p class="holder">
    <span class="holder-name">Liu Wenhao</span>
    <span class="holder-title">China’s Foremost Environmental Preservation Demolition Expert</span>
  </p>

  <div class="band-url">www.jstm.example</div>

  <ul class="contact-list">
    <li class="contact-item">
      <svg class="contact-icon" viewBox="0 0 24 24" aria-label="Phone">
        <path fill="var(--brand-yellow)" d="M6.6 10.8a15.2 15.2 0 0 0 6.6 6.6l2.2-2.2c.3-.3.7-.4 1-.2 1.1.4 2.3.6 3.6.6.6 0 1 .4 1 1V20c0 .6-.4 1-1 1A17 17 0 0 1 3 4c0-.6.4-1 1-1h3.5c.6 0 1 .4 1 1 0 1.3.2 2.5.6 3.6.1.3 0 .7-.2 1z"/>
        <path fill="none" stroke="var(--brand-yellow)" stroke-width="1.6" stroke-linecap="round" d="M14 3.5a6.5 6.5 0 0 1 6.5 6.5M14 7a3 3 0 0 1 3 3"/>
      </svg>
      <span>(+1) 123 456 7890</span>
    </li>
    <li class="contact-item">
      <svg class="contact-icon" viewBox="0 0 24 24" aria-label="Fax">
        <rect x="6" y="3" width="12" height="6" fill="var(--brand-yellow)"/>
        <rect x="2" y="9" width="20" height="10" rx="2" fill="var(--brand-yellow)"/>
        <rect x="6" y="15" width="12" height="6" fill="var(--brand-yellow)" stroke="var(--icon-cut)" stroke-width="1.2"/>
        <circle cx="18.5" cy="12" r="1" fill="var(--icon-cut)"/>
      </svg>
      <span>(+1) 123 456 7890</span>
    </li>
    <li class="contact-item">
      <svg class="contact-icon" viewBox="0 0 24 24" aria-label="Web">
        <rect x="2" y="5" width="20" height="14" rx="1" fill="var(--brand-yellow)"/>
        <path d="M2.5 6l9.5 7 9.5-7" fill="none" stroke="var(--icon-cut)" stroke-width="1.6"/>
      </svg>
      <span>www.jstm.example</span>
    </li>
  </ul>
</div>
</body>
</html>
```